Vesk Architecture

We are a architectural design and build company working between scales 1/1000 to 1/1 we want people to understand our difference from our design experience and quality.we build hotels restourants and office spaces.Our company name is Vesk architecture to mind sustainability.

We want to write our adress phone and work spesifications on the card and we want our logo as backround.

Ps:you could find the logo adress and phone box numbers from the web:www.veskmimarlik-ornek.com

Target Market(s)

Who looks for experts.

Industry/Entity Type

Architecture

Requirements
Must have
• Design is over everything.
Should not have
• we don want it to be colorfull

```html
<!DOCTYPE html>
<html lang="tr">
<head>
<meta charset="utf-8">
<title>Vesk Mimarlık – Business Card</title>
<link rel="stylesheet" href="https://fonts.googleapis.com/css2?family=Source+Sans+3:wght@400&display=swap">
<style>
  :root {
    --page: #ffffff;
    --card-edge: #8a8a8a;
    --teal-deep: #4fbdd6;
    --teal-mid: #7fcfe2;
    --teal-soft: #b4e3ee;
    --ink: #1a1a1a;
    --ink-soft: #3b3b3b;
    --accent: #1f5d99;
    --contact: #2b3a4a;
  }
  * { margin: 0; padding: 0; box-sizing: border-box; }
  html, body {
    width: 1200px; height: 900px; overflow: hidden;
    background: var(--page);
  }
  body { position: relative; font-family: "Source Sans 3", Arial, sans-serif; }

  .business-card {
    position: absolute;
    left: 160px; top: 214px;
    width: 890px; height: 496px;
    border: 2px solid var(--card-edge);
    background: var(--page);
    overflow: hidden;
  }
  .card-background {
    position: absolute; inset: 0;
    background:
      radial-gradient(ellipse 300px 260px at 780px 170px, var(--teal-soft) 0%, rgba(180,227,238,0.55) 55%, rgba(255,255,255,0) 100%),
      radial-gradient(ellipse 340px 220px at 700px 460px, rgba(127,207,226,0.75) 0%, rgba(180,227,238,0.35) 60%, rgba(255,255,255,0) 100%),
      linear-gradient(90deg, var(--teal-deep) 0%, var(--teal-mid) 18%, var(--teal-soft) 36%, rgba(255,255,255,0.9) 52%, var(--page) 62%);
  }

  .brand {
    position: absolute;
    left: 180px; top: 120px;
    color: var(--ink);
    font-weight: 400;
  }
  .brand-name {
    display: block;
    font-size: 168px;
    line-height: 1;
    letter-spacing: -2px;
  }
  .brand-sub {
    display: block;
    margin-top: -6px;
    padding-left: 10px;
    font-size: 34px;
    letter-spacing: 4px;
  }

  .contact-block {
    position: absolute;
    left: 520px; top: 136px;
    width: 340px;
    text-align: center;
  }
  .person-name {
    font-size: 31px;
    color: var(--ink-soft);
    line-height: 1.3;
  }
  .person-role {
    font-size: 31px;
    color: var(--accent);
    line-height: 1.3;
  }
  .contact-list {
    list-style: none;
    margin-top: 42px;
    font-size: 21px;
    line-height: 1.5;
    color: var(--contact);
  }
</style>
</head>
<body>
  <section class="business-card">
    <div class="card-background" role="img" aria-label="Flowing turquoise loop pattern in soft blue tones behind the card"></div>

    <div class="brand">
      <span class="brand-name">vesk</span>
      <span class="brand-sub">MİMARLIK</span>
    </div>

    <div class="contact-block">
      <p class="person-name">Deniz Arman</p>
      <p class="person-role">Manager</p>
      <ul class="contact-list">
        <li>01.0500.314.159</li>
        <li>yourname@veskmimarlik-ornek.com</li>
        <li>www.veskmimarlik-ornek.com</li>
        <li>no 14 street</li>
      </ul>
    </div>
  </section>
</body>
</html>
```